Happy Birthday Postcard for law firm for existing clients

Need a postcard that will go out to our current clients on their birthdays. Prefer to have our logo incorporated as part of the design so it reminds them about our business. The back needs to say "Happy Birthday from the team at Brantley Law Firm."

We are a law firm that services local clients. Needs to be mailed so the backside right half needs to be left blank except the return address (in NEEDS below) so it can be mailed with a mailing label.

Target Market(s)

existing customers, varying age range and demographic profile

Industry/Entity Type

Legal

Font styles to use
Sans Serif
Script

Colors

Designer to choose colors to be used in the design.

Requirements
Must have
• Our logo preferrably on the front (can be modified or added to so it fits a birthday message. And needs to be mailed so the back right side needs to be left open for address labels. The firms return address is
• Brantley Law Firm
• 7150 W Copperfield Ave
• Springfield, MO 65817
• Needs to have the text included in the project description on the back, or some close iteration of it if space is limited.
Nice to have
• Some illustration or graphic on the front with the logo that shows it is a birthday postcard

```html
<!DOCTYPE html>
<html lang="en">
<head>
<meta charset="utf-8">
<title>Brantley Law Firm – Birthday Postcard</title>
<link rel="stylesheet" href="https://fonts.googleapis.com/css2?family=Open+Sans:wght@300;400&family=Yellowtail&family=Dancing+Script:wght@700&display=block">
<style>
  :root {
    --page: #2b2b2d;
    --front-center: #7a16f0;
    --front-edge: #4a06b8;
    --frame: #ffffff;
    --script-shadow: #b51aa6;
    --confetti-yellow: rgba(255, 196, 20, 0.45);
    --confetti-teal: rgba(20, 170, 200, 0.40);
    --confetti-red: rgba(245, 70, 90, 0.40);
    --confetti-green: rgba(90, 200, 60, 0.35);
    --gift-light: #f4ecff;
    --gift-tone: #d58ae6;
    --logo-grey: #7c7a8c;
    --panel-blue: #8e9ab9;
    --panel-grey: #6f7178;
    --card-white: #ffffff;
    --ink: #1f1f22;
    --rule: #9a9a9a;
    --brand-text: #5f6068;
  }
  * { box-sizing: border-box; margin: 0; padding: 0; }
  html, body { width: 816px; height: 1200px; overflow: hidden; }
  body { background: var(--page); position: relative; font-family: "Open Sans", sans-serif; }

  .card { position: absolute; left: 55px; width: 708px; height: 545px; overflow: hidden; }
  .card--front { top: 45px; }
  .card--back { top: 621px; background: var(--card-white); }

  /* Front */
  .front__backdrop {
    position: absolute; inset: 0;
    background: radial-gradient(ellipse at 50% 45%, var(--front-center) 0%, var(--front-edge) 85%);
  }
  .front__confetti {
    position: absolute; inset: 0;
    background:
      radial-gradient(circle at 6% 30%, var(--confetti-yellow) 0, transparent 90px),
      radial-gradient(circle at 10% 75%, var(--confetti-red) 0, transparent 90px),
      radial-gradient(circle at 18% 10%, var(--confetti-teal) 0, transparent 90px),
      radial-gradient(circle at 94% 20%, var(--confetti-red) 0, transparent 90px),
      radial-gradient(circle at 95% 60%, var(--confetti-green) 0, transparent 90px),
      radial-gradient(circle at 88% 88%, var(--confetti-teal) 0, transparent 90px),
      radial-gradient(circle at 50% 4%, var(--confetti-yellow) 0, transparent 80px);
  }
  .front__frame {
    position: absolute; left: 21px; top: 22px; right: 21px; bottom: 22px;
    border: 1.5px solid var(--frame);
  }
  .front__gift {
    position: absolute; left: 440px; top: 38px; width: 104px; height: 116px;
    background: radial-gradient(circle at 45% 40%, var(--gift-light) 0%, var(--gift-light) 35%, var(--gift-tone) 100%);
    border-radius: 14px; transform: rotate(-10deg); opacity: 0.9;
  }
  .front__greeting {
    position: absolute; left: 0; right: 0; top: 118px;
    font-family: "Yellowtail", "Dancing Script", cursive; font-weight: 400;
    color: var(--card-white);
    text-shadow: 8px 12px 0 var(--script-shadow);
    text-align: center; line-height: 0.9;
    transform: rotate(-6deg);
  }
  .front__greeting .line-happy { display: block; font-size: 138px; margin-left: -30px; }
  .front__greeting .line-birthday { display: block; font-size: 132px; margin-left: 50px; }
  .front__brand {
    position: absolute; left: 0; right: 0; top: 484px; text-align: center;
    font-size: 28px; font-weight: 400; letter-spacing: 1px; color: var(--logo-grey);
    text-transform: uppercase;
  }

  /* Back */
  .back__panels { position: absolute; inset: 0; width: 100%; height: 100%; }
  .back__message { position: absolute; left: 41px; top: 20px; color: var(--card-white); font-weight: 300; }
  .back__happy { font-size: 77px; line-height: 1.1; }
  .back__birthday { font-size: 44px; line-height: 1.1; margin-left: 108px; margin-top: 10px; }
  .back__from { font-size: 23px; margin-top: 30px; line-height: 1.2; }
  .back__firm { font-size: 31px; line-height: 1.25; }
  .back__return {
    position: absolute; left: 46px; top: 323px; color: var(--ink); font-style: normal;
    font-size: 20px; font-weight: 400; line-height: 30px;
  }
  .back__brand {
    position: absolute; left: 420px; top: 88px; font-size: 20px; font-weight: 400;
    color: var(--brand-text); text-transform: uppercase; letter-spacing: 0.5px;
  }
  .back__stamp {
    position: absolute; left: 590px; top: 32px; width: 86px; height: 86px;
    border: 1px solid var(--rule);
  }
  .back__address-line { position: absolute; left: 436px; width: 240px; border-top: 1px solid var(--rule); }
  .back__address-line--1 { top: 308px; }
  .back__address-line--2 { top: 356px; }
  .back__address-line--3 { top: 404px; }
</style>
</head>
<body>

<section class="card card--front" aria-label="Postcard front">
  <div class="front__backdrop"></div>
  <div class="front__confetti" role="img" aria-label="Colourful confetti triangles and curling streamers scattered around the edges"></div>
  <div class="front__frame"></div>
  <div class="front__gift" role="img" aria-label="Wrapped gift box with bow"></div>
  <h1 class="front__greeting">
    <span class="line-happy">Happy</span>
    <span class="line-birthday">Birthday!</span>
  </h1>
  <p class="front__brand">Brantley Law</p>
</section>

<section class="card card--back" aria-label="Postcard back">
  <svg class="back__panels" viewBox="0 0 738 568" preserveAspectRatio="none" aria-hidden="true">
    <polygon points="0,0 433,0 293,568 0,568" fill="var(--panel-blue)"/>
    <polygon points="433,0 338,568 293,568" fill="var(--panel-grey)"/>
  </svg>

  <div class="back__message">
    <p class="back__happy">Happy</p>
    <p class="back__birthday">Birthday</p>
    <p class="back__from">from the team at</p>
    <p class="back__firm">Brantley Law Firm</p>
  </div>

  <address class="back__return">
    Brantley Law Firm<br>
    7150 W Copperfield Ave<br>
    Springfield, MO 65817
  </address>

  <p class="back__brand">Brantley Law</p>
  <div class="back__stamp" aria-label="Stamp area"></div>

  <div class="back__address-line back__address-line--1"></div>
  <div class="back__address-line back__address-line--2"></div>
  <div class="back__address-line back__address-line--3"></div>
</section>

</body>
</html>
```